Web site for mobile& web developers

We need a web site design for our company, Tamblin Reef Works Pty Ltd.

We are a Sydney based, software development company specialising in mobile platforms and web applications. We are a small, dynamic team with a few awesome products we want to get out to the world.

We would prefer a clean, professional layout that incorporates the company logo and branding; we do have a youthful, start-up edge which we would like to express.

We technical people with damn good products, so your design has to make us look good to non-technical people too!

Target Market(s)

B2B, Enterprise technology, Project Managers, Marketing, Other developers

Industry/Entity Type

It Company

Requirements
Must have
• Required pages:
- home page - this must allow us to feature our software (mobile & web) on the home page
- a standard content page (for things like "about us", "our team", etc)
- contact us (including HTML form with error state)
- mobile (iOS and Android) product page - allow for screen shots, features, requirements, customer list
- web product page - allow for screen shots, features, requirements, customer list

You must incorporate our logo and branding into the theme.
Should not have
• HTML/CSS carve is not required. We only required layered PNGs or PSDs.

```html
<!DOCTYPE html>
<html lang="en">
<head>
<meta charset="utf-8">
<title>Tamblin Reef Works – About Us</title>
<link rel="stylesheet" href="https://fonts.googleapis.com/css2?family=PT+Sans:ital,wght@0,400;0,700;1,400;1,700&family=Fira+Sans:ital,wght@1,700&display=swap">
<style>
:root{
  --blue:#1d6fb8;
  --nav-active:#1a78c2;
  --teal-head:#3b6f87;
  --dark-head:#3a3a3a;
  --light-head:#777;
  --orange:#e2652a;
  --text:#111;
  --light-bg:#f3f3f3;
  --band:#e9e9e9;
  --client-band:#dcdcdc;
  --footer:#4a4a4a;
  --footer-text:#e8e8e8;
  --side-active:#8db0de;
  --rule:#c9c9c9;
}
*{margin:0;padding:0;box-sizing:border-box}
html,body{width:1200px;height:1012px;overflow:hidden}
body{font-family:"PT Sans",sans-serif;color:var(--text);background:#fff;position:relative}
.wrap{position:absolute;left:196px;width:804px}
.stripe{height:5px;background:repeating-linear-gradient(90deg,#2d7fc8 0 6px,#9cc4ea 6px 9px,#1e5f9e 9px 13px,#d7e7f6 13px 16px)}
.header{position:absolute;top:5px;left:0;width:1200px;height:105px;background:var(--light-bg)}
.brand{position:absolute;left:8px;top:42px;display:flex;align-items:center;gap:12px;font-size:25px;letter-spacing:3px;color:#666}
.brand-mark{width:34px;height:34px;border-radius:50%;background:#3a9ad9}
.contact{position:absolute;right:14px;top:14px;font-size:13px;color:var(--blue);font-weight:700;line-height:16px}
.contact div{display:flex;align-items:center;gap:8px}
.nav{position:absolute;right:0;top:67px;height:28px;border:1px solid var(--blue);display:flex;font-size:11.5px;background:#fff}
.nav a{display:block;padding:0 10px;line-height:26px;color:#111;text-decoration:none}
.nav a.active{background:var(--nav-active);color:#fff}
.hero{position:absolute;top:110px;left:0;width:1200px;height:171px;background:linear-gradient(#f7f7f7,#ececec)}
.hero h1{position:absolute;left:210px;top:42px;font-family:"Fira Sans",sans-serif;font-style:italic;font-weight:700;font-size:27px;line-height:37px;color:var(--orange)}
.hero-photo{position:absolute;left:586px;top:0;width:414px;height:171px;background:linear-gradient(90deg,#d9c7b4,#8a9fb8 45%,#3a5f8e 75%,#c8b49d)}
.subband{position:absolute;top:281px;left:0;width:1200px;height:31px;background:var(--band);border-top:1px solid #dadada;border-bottom:1px solid #dadada}
.about{top:340px;width:532px}
.about h2{font-size:20px;font-weight:400;margin-bottom:4px;display:flex;align-items:center;gap:6px}
.about h2 .a{color:var(--teal-head)}
.about h2 .b{color:var(--dark-head)}
.about h2 .c{color:var(--light-head)}
.about h2 i{width:26px;height:26px;border-radius:50%;background:#3a9ad9;display:inline-block;margin-left:4px}
.about p{font-size:11px;line-height:14.2px;margin-bottom:14px}
.side{position:absolute;left:805px;top:345px;width:195px}
.side h3{font-size:16px;font-weight:700;margin-bottom:12px}
.side ul{list-style:none;font-size:11px}
.side li{border-bottom:1px solid var(--rule);padding:0 4px;line-height:26px}
.side li.open{background:var(--side-active);line-height:22px;border:none;margin-left:2px}
.side .panel{display:flex;justify-content:space-between;padding:8px 8px 6px 6px;border-bottom:1px solid var(--rule);background:linear-gradient(90deg,#fff,#f1f1f1);font-size:9px;line-height:11.5px;margin-left:2px}
.side .panel b{display:block;margin-top:5px}
.phone-shot{width:40px;height:56px;border-radius:6px;background:linear-gradient(135deg,#4a7aa8,#1c2f44)}
.clients{position:absolute;top:693px;left:0;width:1200px;height:78px;background:var(--client-band)}
.clients .row{position:absolute;left:210px;width:780px;top:0;height:78px;display:flex;align-items:center;justify-content:space-between;font-weight:700;font-size:15px;color:#1b1b1b}
.clients .row span{display:flex;align-items:center;gap:6px}
.clients .sq{width:12px;height:12px;background:#2a3f7a}
.footer{position:absolute;top:771px;left:0;width:1200px;height:162px;background:var(--footer);color:var(--footer-text);border-top:4px solid #5a5a5a}
.footer h4{position:absolute;font-size:13px;font-weight:700;white-space:nowrap}
.footer .abs{position:absolute}
.quote-text{left:197px;top:48px;width:225px;font-style:italic;font-size:11px;line-height:14.2px}
.who{left:197px;top:124px;font-weight:700;font-size:11px;line-height:14.5px}
.viewall{font-size:11px;font-weight:700}
.divider{position:absolute;top:14px;height:135px;border-left:1px dotted #777}
.icons{left:554px;top:33px;display:grid;grid-template-columns:repeat(4,22px);gap:6px 7px}
.icons i{display:block;width:22px;height:22px;border-radius:3px;background:#6a8fbf}
.email{left:540px;top:122px;display:flex;align-items:center;width:138px;height:21px;border-radius:11px;background:#fff;color:#222;font-size:9px;font-weight:700;padding-left:9px;justify-content:space-between}
.email span.go{width:22px;height:21px;border-radius:50%;background:#5d95cc;color:#fff;display:flex;align-items:center;justify-content:center;font-size:9px}
.bird{left:808px;top:16px;width:20px;height:20px;border-radius:50%;background:#2b2b2b}
.tweets{left:808px;top:40px;width:192px;font-size:9.3px;line-height:12px}
.tweets p{border-bottom:1px dotted #888;padding-bottom:4px;margin-bottom:5px}
.bottom{position:absolute;top:933px;left:0;width:1200px;height:79px;background:linear-gradient(#f5f5f5 0 84%,#e3e3e3 84%)}
.bottom .wrap{top:27px;display:flex;justify-content:space-between;font-size:11px;font-weight:700;color:#555}
.bottom nav a{color:#555;text-decoration:none}
</style>
</head>
<body>
<div class="stripe"></div>

<header class="header">
  <div class="wrap" style="top:0;height:105px">
    <div class="brand"><span>TAMBLIN REEF WORKS</span><span class="brand-mark"></span></div>
    <div class="contact">
      <div><svg width="10" height="9" viewBox="0 0 10 9"><path d="M1 3q4-3 8 0v2H7V4H3v1H1z M2 5h6v4H2z" fill="#8aaed3"/></svg>+61 2 5550 1234</div>
      <div><svg width="10" height="10" viewBox="0 0 10 10"><circle cx="5" cy="5" r="4.2" fill="none" stroke="#8aaed3"/><path d="M1 5h8M5 1v8" stroke="#8aaed3"/></svg>info@tamblinreef.com</div>
    </div>
    <nav class="nav">
      <a href="#">Home</a><a href="#" class="active">About Us</a><a href="#">News</a><a href="#">Products</a><a href="#">Contact Us</a>
    </nav>
  </div>
</header>

<section class="hero">
  <h1>We are passionate about<br>quality products...</h1>
  <div class="hero-photo" role="img" aria-label="Photo of a smiling team giving thumbs up"></div>
</section>
<div class="subband"></div>

<main class="wrap about">
  <h2><span class="a">ABOUT</span> <span class="b">TAMBLIN REEF</span> <span class="c">WORKS</span><i></i></h2>
  <p>We are passionate about quality products. Our core focus is on producing quality user centric products from your ideas. Bleeding edge technologies, high-volume consumer digital products and knowing your audience are our bread and butter. We are the leading online and mobile technology BPO in the Asia Pacific region. We have the passion, the talent and the network to make your idea the next big thing.</p>
  <p>Lorem Ipsum is simply dummy text of the printing and typesetting industry. Lorem Ipsum has been the industry's standard dummy text ever since the 1500s, when an unknown printer took a galley of type and scrambled it to make a type specimen book. It has survived not only five centuries, but also the leap into electronic typesetting, remaining essentially unchanged.</p>
  <p>Lorem Ipsum is simply dummy text of the printing and typesetting industry. Lorem Ipsum has been the industry's standard dummy text ever since the 1500s, when an unknown printer took a galley of type and scrambled it to make a type specimen book. It has survived not only five centuries, but also the leap into electronic typesetting, remaining essentially unchanged. It was popularised in the 1960s with the release of Bramwell Press sheets containing Lorem Ipsum passages, and more recently with desktop publishing software like Folio Layout Studio including versions of Lorem Ipsum.</p>
  <p>Lorem Ipsum is simply dummy text of the printing and typesetting industry. Lorem Ipsum has been the industry's standard dummy text ever since the 1500s, when an unknown printer took a galley of type and scrambled it to make a type specimen book. It has survived not only five centuries.</p>
</main>

<aside class="side">
  <h3>WORK WITH US:</h3>
  <ul>
    <li class="open">&#8594; MOBILE</li>
    <li class="panel">
      <div>Lorem Ipsum is simply dummy<br>text of the printing and type-<br>setting industry.<b>+ Read More</b></div>
      <div class="phone-shot" role="img" aria-label="Illustration of a smartphone"></div>
    </li>
    <li>&#8594; PYTHON</li>
    <li style="border:none;line-height:34px">&#8594; DIGITAL EXPERIENCE</li>
  </ul>
</aside>

<section class="clients">
  <div class="row">
    <span><i class="sq"></i>Harbour Soft</span>
    <span>Northwind Systems</span>
    <span>Kestrel Digital</span>
    <span>Meridian Screen Guild</span>
    <span><i class="sq"></i>Harbour Soft</span>
    <span>Northwind Systems</span>
  </div>
</section>

<footer class="footer">
  <h4 style="left:197px;top:14px">What our Client Says About Us...</h4>
  <p class="abs quote-text">&ldquo; Lorem Ipsum is simply dummy text of the printing and typesetting industry. Lorem Ipsum has been the industry's standard dummy text ever since the including versions of Lorem Ipsum. &rdquo;</p>
  <p class="abs who">Dana Whitlock<br>C.E.O. Northwind Systems</p>
  <span class="abs viewall" style="left:357px;top:139px">+ View All</span>

  <div class="divider" style="left:477px"></div>

  <h4 style="left:554px;top:14px">Connect Us...</h4>
  <div class="abs icons"><i></i><i style="background:#d9822b"></i><i style="background:#6fb6e0"></i><i style="background:#2f76b0"></i><i style="background:#ddd"></i><i style="background:#6a9a3c"></i><i style="background:#b33"></i><i style="background:#e6e6e6"></i></div>
  <h4 style="left:540px;top:98px">Signup for Newsletter:</h4>
  <div class="abs email">Enter Email...<span class="go">Go</span></div>

  <div class="divider" style="left:738px"></div>

  <span class="abs bird"></span>
  <h4 style="left:834px;top:17px">Latest Tweets:</h4>
  <div class="abs tweets">
    <p>Lorem Ipsum is simply dummy text of the printing and typesetting industry.</p>
    <p>Lorem Ipsum is simply dummy text of the printing and typesetting industry.</p>
    <p style="border:none">Lorem Ipsum is simply dummy text of the printing and typesetting industry.</p>
  </div>
  <span class="abs viewall" style="left:938px;top:139px">+ View All</span>
</footer>

<div class="bottom">
  <div class="wrap">
    <span>&copy; Copyright Tamblin Reef Works | All Rights Reserved</span>
    <nav><a href="#">Home</a> &nbsp;|&nbsp; <a href="#">About Us</a> &nbsp;|&nbsp; <a href="#">Contact Us</a></nav>
  </div>
</div>
</body>
</html>
```